Postcard Design

Pebble Pockets is a boutique selling childrens toys and clothing. We have a lot of well known kids fashion labels such as Tavro K, Quibble, Zorbi, Pine Hollow Sandals, Brambleton Kids and many more.
Save 10% when you shop online at www.pebblepocketsshop.example. Use the code 7bonus at the check out.
47 Larkspur Road, West Dunmore NSW 2271 ph 02 49817362

Industry/Entity Type

Boutique

```html
<!DOCTYPE html>
<html lang="en">
<head>
<meta charset="utf-8">
<title>Pebble Pockets Postcard</title>
<link rel="stylesheet" href="https://fonts.googleapis.com/css2?family=Dosis:wght@500;600;700&family=Arimo:wght@400;700&display=swap">
<style>
  :root {
    --maroon: #8c1f2d;
    --maroon-bright: #a9202f;
    --yellow: #f7c51e;
    --teal: #4cbfcb;
    --white: #ffffff;
    --ink: #111111;
    --page: #ecebe8;
    --sky: #8fc3ea;
    --dress: #e8792a;
  }
  * { box-sizing: border-box; margin: 0; padding: 0; }
  html, body { width: 1200px; height: 846px; overflow: hidden; }
  body { background: var(--page); position: relative; font-family: "Dosis", sans-serif; }

  .card { position: absolute; width: 560px; height: 396px; background: var(--white); overflow: hidden; box-shadow: 0 2px 10px rgba(0,0,0,.15); }
  .card--front { left: 30px; top: 225px; }
  .card--back { left: 610px; top: 225px; }

  /* Front */
  .front-photo { position: absolute; left: 130px; top: 0; width: 430px; height: 396px;
    background: linear-gradient(180deg, var(--sky) 0%, #cfe3ef 45%, #c9a77e 75%, #9a7a55 100%); }
  .front-photo__subject { position: absolute; left: 110px; top: 150px; width: 200px; height: 246px; border-radius: 90px 90px 0 0;
    background: linear-gradient(180deg, #f0a050, var(--dress)); }
  .product { position: absolute; border-radius: 50%; }
  .product--romper { left: 330px; top: 110px; width: 100px; height: 100px; background: #bfe6ee; }
  .product--toy { left: 320px; top: 250px; width: 100px; height: 100px; background: #efd3e0; }
  .front-panel { position: absolute; left: 0; top: 0; width: 190px; height: 396px; }
  .front-panel svg { position: absolute; inset: 0; }
  .brand { position: absolute; left: 16px; top: 52px; display: flex; align-items: center; gap: 8px; }
  .brand__dot { width: 18px; height: 18px; border-radius: 50%; background: var(--white); }
  .brand__name { color: var(--white); font-weight: 700; font-size: 20px; letter-spacing: .5px; }
  .front-url { position: absolute; left: 12px; top: 118px; width: 160px; color: var(--white); font-size: 11px; font-weight: 600; }
  .offer { position: absolute; left: 10px; top: 148px; width: 160px; text-align: center; color: var(--white); font-size: 17px; font-weight: 600; line-height: 1.25; }
  .offer__save { color: var(--yellow); }
  .offer__code { display: inline-block; border: 1.5px dashed var(--yellow); padding: 0 5px; margin: 2px 0; }
  .range { position: absolute; left: 14px; top: 330px; width: 155px; text-align: center; color: var(--teal); font-size: 12px; font-weight: 600; line-height: 1.3; }

  /* Back */
  .back-band { position: absolute; left: 0; top: 0; width: 320px; height: 140px; }
  .back-band svg { position: absolute; inset: 0; }
  .back-brand { position: absolute; left: 60px; top: 45px; display: flex; align-items: center; gap: 8px; }
  .back-brand .brand__name { font-size: 19px; }
  .back-contact { position: absolute; left: 28px; top: 143px; color: var(--teal); font-family: "Arimo", sans-serif; font-size: 8.5px; line-height: 1.6; }
  .back-contact__url { display: block; text-align: center; font-weight: 700; font-size: 9.5px; }
  .postage { position: absolute; right: 28px; top: 48px; width: 110px; text-align: center; font-family: "Arimo", sans-serif; font-size: 9px; line-height: 1.25; color: var(--ink); }
  .postage__bars { display: flex; justify-content: center; gap: 12px; margin-top: 12px; }
  .postage__bars span { width: 8px; height: 70px; background: var(--ink); }
  .letter { position: absolute; left: 28px; top: 195px; width: 230px; font-family: "Arimo", sans-serif; font-size: 10px; line-height: 1.35; color: var(--ink); }
  .letter p { margin-bottom: 10px; }
  .recipient { position: absolute; left: 300px; top: 262px; font-family: "Arimo", sans-serif; font-size: 15.5px; line-height: 1.15; color: var(--ink); }
</style>
</head>
<body>

<section class="card card--front" aria-label="Postcard front">
  <div class="front-photo" role="img" aria-label="Photo of a curly-haired toddler in a floral top playing outdoors">
    <div class="front-photo__subject"></div>
    <div class="product product--romper" role="img" aria-label="Product image of a navy kids romper"></div>
    <div class="product product--toy" role="img" aria-label="Product image of a red toy coffee machine"></div>
  </div>
  <div class="front-panel">
    <svg viewBox="0 0 190 396" width="190" height="396" aria-hidden="true">
      <path d="M0 0 H150 Q160 40 150 80 Q140 120 152 160 Q164 200 150 240 Q138 280 152 320 Q164 360 155 396 H0 Z" fill="var(--maroon)"/>
    </svg>
    <div class="brand"><span class="brand__dot"></span><span class="brand__name">Pebble Pockets</span></div>
    <p class="front-url">www.pebblepocketsshop.example</p>
    <p class="offer">
      <span class="offer__save">Save 10%</span><br>
      when you shop online.<br>
      Use the code<br>
      <span class="offer__code">7bonus</span><br>
      at the check out.
    </p>
    <p class="range">Childrens toys,<br>Kids fashions, books<br>and many more.</p>
  </div>
</section>

<section class="card card--back" aria-label="Postcard back">
  <div class="back-band">
    <svg viewBox="0 0 320 140" width="320" height="140" aria-hidden="true">
      <path d="M0 0 H320 V120 Q305 132 290 122 Q275 112 260 124 Q245 136 230 124 Q215 112 200 124 Q185 136 170 124 Q155 112 140 124 Q125 136 110 124 Q95 112 80 124 Q65 136 50 124 Q35 112 20 124 Q10 132 0 126 Z" fill="var(--maroon-bright)"/>
    </svg>
    <div class="back-brand"><span class="brand__dot"></span><span class="brand__name">Pebble Pockets</span></div>
  </div>
  <p class="back-contact">47 Larkspur Road, West Dunmore NSW 2271 &nbsp;p 02 49817362
    <span class="back-contact__url">www.pebblepocketsshop.example</span></p>
  <div class="postage">No stamp required<br>if posted in Australia
    <div class="postage__bars"><span></span><span></span><span></span></div>
  </div>
  <div class="letter">
    <p>Dear Value Customer,</p>
    <p>Lorem ipsum dolor sit amet, consectetur adipiscing elit, sed do eiusmod tempor incididunt ut labore et dolore magna aliqua.</p>
    <p>Ut enim ad minim veniam, quis nostrud exercitation ullamco laboris nisi ut aliquip ex ea commodo consequat.</p>
    <p>Looking forward to seeing you.</p>
  </div>
  <p class="recipient">CUSTOMER NAME<br>1277 INDUSTRIAL DR<br>ANY CITY NSW 2250</p>
</section>

</body>
</html>
```